Squeeze page design

We need to design some squeeze pages for our list building campaigns. We use Ledgerbay as our crm. Our squeeze pages really suck. We simply need to design some pages that look better and will convert, better than what we are currently using.
The landing page that we are trying to replace can be seen at:
http://shieldworksco.example/multi-family-landing-1
The sign up page that we need to replace is:
http://shieldworksco.example/free-multi-family-offer
Our thought is that the landing page and sign up page should be combined into a single squeeze page that will improve conversions - conversions being sign ups.
Updates
Project Deadline Extended
Reason: I have had some requests to extend my deadline and I need to have some updates made to some of the submissions. Thank you.
Industry/Entity Type
Building
Look and feel
Each slider illustrates characteristics of the customer's brand and the style your logo design should communicate.

```html
<!DOCTYPE html>
<html lang="en">
<head>
<meta charset="utf-8">
<title>ShieldWorks Co – Multi-Family Free Offer</title>
<link href="https://fonts.googleapis.com/css2?family=Open+Sans:ital,wght@0,400;0,600;0,700;1,400;1,600&display=swap" rel="stylesheet">
<style>
:root{
  --ink:#333;
  --muted:#9a9a9a;
  --teal:#1a6f7e;
  --cyan:#2fc4dc;
  --dark:#1f1f1f;
  --darker:#161616;
  --band:#f4f3ee;
  --line:#e3e3e3;
  --red:#d9131a;
  --blue:#2b7fc0;
  --white:#fff;
}
*{box-sizing:border-box;margin:0;padding:0}
html,body{width:1200px;height:3377px;overflow:hidden}
body{font-family:"Open Sans",Arial,sans-serif;color:var(--ink);background:var(--white);font-size:14px;line-height:1.5}
.wrap{width:984px;margin:0 auto;position:relative}
a{color:inherit;text-decoration:none}

.topbar{height:32px;background:var(--darker);color:#ccc;font-size:12px}
.topbar .wrap{display:flex;justify-content:space-between;align-items:center;height:32px}
.topbar nav a{margin-right:10px;padding-right:10px;border-right:1px solid #555;color:#eee;font-weight:600}
.topbar nav a:last-child{border:none}

.header{height:108px;background:linear-gradient(#fafafa,#dcdcdc);border-bottom:1px solid #bbb}
.header .wrap{height:108px}
.brand{position:absolute;left:0;top:24px;display:flex;align-items:center;gap:10px}
.brand-mark{width:34px;height:34px;background:#222}
.brand-name{font-size:22px;font-weight:700;color:#222}
.brand-tag{margin-left:14px;font-size:13px;font-weight:600;color:#666}
.made-in{position:absolute;right:0;top:14px;background:#2a2a2a;color:#fff;font-weight:700;font-size:14px;padding:5px 14px;border-radius:3px}
.mainnav{position:absolute;right:0;top:66px;font-size:12px;color:#555}
.mainnav a{margin-left:22px}
.mainnav a.current{color:#111;font-weight:600}

.hero{height:508px;position:relative;background:linear-gradient(110deg,#2e2e2e 0%,#6a6a6a 40%,#bdbdbd 60%,#4a4a4a 100%)}
.hero-photo{position:absolute;inset:0}
.hero-caption{position:absolute;left:108px;bottom:14px;color:#fff;font-size:32px;font-weight:600;background:rgba(0,0,0,.35);padding:4px 14px 4px 0;width:630px}
.hero-caption span{color:var(--cyan)}
.offer{position:absolute;left:738px;top:0;width:354px;height:508px;background:rgba(20,20,20,.82);padding:20px 0 0 20px;color:#fff}
.offer h2{font-size:26px;font-weight:400;margin-bottom:8px}
.offer p{font-size:12px;line-height:1.5;color:#ddd;width:320px;margin-bottom:10px}
.field{display:block;background:#fff;height:34px;width:314px;margin-bottom:9px;font-size:11px;color:#999;padding:8px 10px}
.field-row{display:flex;gap:8px}
.field-row .field{width:153px}
.field.tall{height:112px}
.offer .btns{display:flex;gap:10px;margin-top:14px}
.btn{background:var(--blue);color:#fff;font-weight:700;font-size:14px;width:122px;height:34px;line-height:34px;text-align:center}

.featured{padding:28px 0 0;height:218px}
.section-title{font-size:19px;font-weight:600;color:#333;display:flex;align-items:center;gap:14px}
.section-title::after{content:"";flex:1;height:1px;background:var(--line)}
.logo-strip{display:flex;align-items:center;gap:30px;margin-top:26px}
.circle-btn{width:40px;height:40px;border-radius:50%;background:#bdbdbd;color:#fff;display:flex;align-items:center;justify-content:center}
.press-badge{width:105px;height:38px;background:#d5d5d5}

.promo{background:#e9e9e9;border:1px solid #ddd;height:162px;text-align:center;padding:16px 40px}
.promo p{font-style:italic;font-size:15px;color:#555;line-height:1.5}
.promo em{color:var(--teal);font-style:italic}
.promo-cta{display:inline-block;margin-top:18px;background:var(--red);color:#fff;font-weight:700;font-style:italic;font-size:18px;padding:8px 26px;border:2px solid #a00}

.intro{display:flex;gap:30px;padding:36px 0 0;height:414px}
.col-left{width:560px}
.col-right{flex:1}
.intro h3{font-size:19px;font-weight:600;margin-bottom:24px}
.video{height:312px;background:linear-gradient(135deg,#3a3a3a,#7a7a7a 50%,#2a2a2a);position:relative}
.video-bar{position:absolute;left:0;right:0;bottom:0;height:36px;background:rgba(0,0,0,.75)}
.video-progress{position:absolute;left:90px;top:15px;width:340px;height:6px;background:#2a8fb3}
.point{color:var(--teal);font-size:16px;line-height:1.4}
.note{font-size:12px;color:var(--muted);margin:4px 0 18px}
.more{font-size:12px;color:#666;text-decoration:underline}

.police{background:var(--band);height:578px;padding-top:40px;margin-top:-5px}
.center-title{text-align:center;font-size:30px;font-weight:600;color:#333}
.lede{text-align:center;font-size:13.5px;color:var(--muted);width:880px;margin:14px auto 0;line-height:1.6}
.police-body{display:flex;gap:50px;margin-top:40px}
.tablet{width:520px;height:320px;background:#1c1c1c;border-radius:14px 14px 0 0;padding:12px 12px 0}
.tablet-screen{height:100%;background:linear-gradient(135deg,#2c3a4a,#6a5a50 50%,#20262e)}
.features{flex:1}
.features h4{color:var(--teal);font-size:17px;font-weight:400;margin-top:6px}
.features p{font-size:12px;color:var(--muted);line-height:1.6;margin:4px 0 6px}

.available{height:180px;padding-top:34px;border-bottom:1px solid var(--line)}
.available .center-title{font-size:22px}
.available .lede{margin-top:10px}

.products{display:flex;padding:30px 0 0;height:360px}
.product{flex:1;padding:0 22px;border-left:1px solid var(--line)}
.product:first-child{padding-left:0;border:none}
.product h4{font-size:19px;font-weight:400;margin-bottom:16px}
.product-img{height:122px;background:linear-gradient(90deg,#1c2a3a,#4d6a88)}
.product p{font-size:12px;color:#666;line-height:1.55;margin-top:12px}

.clients{background:var(--band);height:484px;padding-top:50px}
.clients .center-title{font-size:22px}
.quotes{display:flex;gap:34px;margin-top:48px}
.quote{flex:1}
.quote-box{background:#fff;border:1px solid #e6e6e6;height:146px;padding:26px 18px 20px 22px;font-size:13px;line-height:1.7;color:#444;position:relative}
.quote-box::before{content:"\201C";position:absolute;left:8px;top:-4px;font-size:26px;color:#999}
.quote-box::after{content:"\201D";position:absolute;right:10px;bottom:-14px;font-size:26px;color:#999}
.person{display:flex;align-items:center;gap:14px;margin-top:20px}
.avatar{width:56px;height:56px;border-radius:50%;background:#c9b8a8}
.person b{display:block;font-weight:400;color:var(--teal);font-size:13px}
.person span{font-size:12px;color:#555}

.footer{background:var(--dark);height:227px;color:#999;padding-top:42px}
.footer .wrap{display:flex}
.fcol{width:170px}
.fcol.wide{width:300px}
.fcol.last{flex:1}
.fcol h5{color:#eee;font-size:15px;font-weight:600;margin-bottom:10px}
.fcol a,.fcol p{display:block;font-size:12px;line-height:1.85}
.fcol .split{display:flex;gap:30px}
.seal{display:inline-block;width:60px;height:34px;background:#4c6ea0;margin:8px 8px 0 0}
.seal.sm{width:36px;background:#6a8fc2}
.bottombar{height:52px;background:var(--darker);color:#777;font-size:11px}
.bottombar .wrap{display:flex;justify-content:space-between;align-items:center;height:52px}
.cards{display:flex;gap:6px}
.cards span{width:38px;height:22px;background:#ccc;border-radius:2px}
</style>
</head>
<body>

<div class="topbar"><div class="wrap">
  <nav><a href="#">FAQ</a><a href="#">Store</a><a href="#">Installer Locator</a><a href="#">Affiliates</a><a href="#">Register</a><a href="#">Login</a></nav>
  <div>24/7 Customer Service 888-555-0147 &nbsp;|&nbsp; info@shieldworksco.example</div>
</div></div>

<header class="header"><div class="wrap">
  <div class="brand"><span class="brand-mark"></span><span class="brand-name">ShieldWorks Co</span><span class="brand-tag">Doors Done Right</span></div>
  <div class="made-in">MADE IN U.S.A</div>
  <nav class="mainnav"><a class="current" href="#">HOME</a><a href="#">BUY ONLINE</a><a href="#">PREVENTING BREAK INS</a><a href="#">TESTIMONIALS</a><a href="#">ABOUT US</a><a href="#">OUR BLOG</a></nav>
</div></header>

<section class="hero">
  <div class="hero-photo" role="img" aria-label="Gloved hand forcing a pry bar against an apartment door lock"></div>
  <div class="hero-caption">Guaranteed To <span>Save You Money!</span></div>
  <form class="offer">
    <h2>Multi-Family Free Offer</h2>
    <p>Complete this form and ShieldWorks Co will send you a free property quote and our security consultant can ship your property a sample kit.</p>
    <span class="field">Property Name:</span>
    <div class="field-row"><span class="field">First Name:</span><span class="field">Last Name:</span></div>
    <span class="field">Email:</span>
    <span class="field">Phone Number:</span>
    <span class="field tall">Total Number Of Units:</span>
    <div class="btns"><span class="btn">SUBMIT</span><span class="btn">RESET</span></div>
  </form>
</section>

<section class="featured"><div class="wrap">
  <h3 class="section-title">As Featured On</h3>
  <div class="logo-strip">
    <span class="circle-btn"><svg width="14" height="14" viewBox="0 0 14 14"><path d="M9 2 4 7l5 5" stroke="#fff" stroke-width="2.5" fill="none"/></svg></span>
    <span class="press-badge"></span><span class="press-badge"></span><span class="press-badge"></span><span class="press-badge" style="width:190px"></span><span class="press-badge"></span><span class="press-badge"></span>
    <span class="circle-btn"><svg width="14" height="14" viewBox="0 0 14 14"><path d="m5 2 5 5-5 5" stroke="#fff" stroke-width="2.5" fill="none"/></svg></span>
  </div>
</div></section>

<div class="wrap">
  <div class="promo">
    <p><em>Guaranteed to Save You Money!</em> * Safety is the number 1 reason residents site for moving. * We secure the multi-family world * <em>Police Recommended</em> * More than 50,000 sold * We are offering first-time multi-family customers a <em>FREE SAMPLE</em>. Have your biggest guys put us to the test!</p>
    <svg width="60" height="30" viewBox="0 0 60 30" style="vertical-align:middle;margin-right:14px"><path d="M2 4c10 18 30 20 52 18m-6-6 6 6-6 6" stroke="#888" stroke-width="1.5" fill="none"/></svg><a class="promo-cta" href="#">Free Sample - Click Here</a>
  </div>

  <section class="intro">
    <div class="col-left">
      <h3>Apartment Security Starts Here</h3>
      <div class="video" role="img" aria-label="Video of a pry bar attack on a reinforced door frame">
        <div class="video-bar"><svg width="30" height="36" viewBox="0 0 30 36" style="margin-left:24px"><path d="M10 12v12l10-6z" fill="#fff"/></svg><span class="video-progress"></span></div>
      </div>
    </div>
    <div class="col-right">
      <h3>Why Secure Your Doors?</h3>
      <div class="point">Safety is the #1 reason residents site for moving</div>
      <div class="note">More than 85% of all break-ins are through a door.</div>
      <div class="point">It costs more than $4,000 to replace a single resident</div>
      <div class="note">Residents in "Good properties" are 10x more likely to relocate on news of crime in the community!<br><br>Only ShieldWorks Co has solutions to fit every budget. Whether you're looking for security or repair, we will save you money.</div>
      <a class="more" href="#">Read More</a>
    </div>
  </section>
</div>

<section class="police"><div class="wrap">
  <h2 class="center-title">Why Police Trust Us</h2>
  <p class="lede">Lorem ipsum dolor sit amet, consectetur adipisicing elit, sed do eiusmod tempor incididunt ut labore et dolore magna aliqua. Ut enim ad minim veniam, quis nostrud exercitation do eiusmod tempor incididunt ut labore et dolore magna aliqua ullamco laboris nisi ut aliquip ex ea commodo consequat.</p>
  <div class="police-body">
    <div class="tablet"><div class="tablet-screen" role="img" aria-label="Video interview with a police officer recommending the product"></div></div>
    <div class="features">
      <h4>Police Tested and Recommended</h4>
      <p>Lorem ipsum dolor sit amet, consectetur adipisicing elit, sed do eiusmod tempor incididunt ut labore et dolore magna aliqua.</p>
      <a class="more" href="#">Read More</a>
      <h4 style="margin-top:18px">Lifetime Warranty</h4>
      <p>Lorem ipsum dolor sit amet, consectetur adipisicing elit, sed do eiusmod tempor incididunt ut labore et dolore magna aliqua.</p>
      <a class="more" href="#">Read More</a>
      <h4 style="margin-top:18px">Attractive Finish Options</h4>
      <p>Lorem ipsum dolor sit amet, consectetur adipisicing elit, sed do eiusmod tempor incididunt ut labore et dolore magna aliqua.</p>
      <a class="more" href="#">Read More</a>
    </div>
  </div>
</div></section>

<section class="available"><div class="wrap">
  <h2 class="center-title">Available For All Doors and Budgets</h2>
  <p class="lede">Lorem ipsum dolor sit amet, consectetur adipisicing elit, sed do eiusmod tempor incididunt ut labore et dolore magna aliqua. Ut enim ad minim veniam, quis nostrud exercitation do eiusmod tempor incididunt ut labore et dolore magna aliqua ullamco laboris nisi ut aliquip ex ea commodo consequat.</p>
</div></section>

<section class="wrap products">
  <article class="product"><h4>EZ Guard Combo Set</h4><div class="product-img" role="img" aria-label="Combo set product shot with door hardware"></div><p>Donec consectetur libero tortor condimentum egestas viverra sed. Dolor sit amet consectetur adipisicing elit, Sed do eiusmod tempor incididunt magna aliqua..</p></article>
  <article class="product"><h4>Jamb Fix Kit</h4><div class="product-img" style="background:linear-gradient(90deg,#111,#333 60%,#ddd 62%,#222)" role="img" aria-label="Jamb repair kit product shot"></div><p>Donec consectetur libero tortor condimentum egestas viverra sed. Dolor sit amet consectetur adipisicing elit, Sed do eiusmod tempor incididunt magna aliqua..</p></article>
  <article class="product"><h4>Shield Latch</h4><div class="product-img" style="background:linear-gradient(90deg,#2a2a2a,#8a8a8a 60%,#e8e8e8)" role="img" aria-label="Door latch guard product shot"></div><p>Donec consectetur libero tortor condimentum egestas viverra sed. Dolor sit amet consectetur adipisicing elit, Sed do eiusmod tempor incididunt magna aliqua..</p></article>
</section>

<section class="clients"><div class="wrap">
  <h2 class="center-title">What Our Client Say</h2>
  <p class="lede">Lorem ipsum dolor sit amet, consectetur adipisicing elit, sed do eiusmod tempor incididunt ut labore et dolore magna aliqua. Ut enim ad minim veniam, quis nostrud exercitation do eiusmod tempor incididunt ut labore et dolore magna aliqua ullamco laboris nisi ut aliquip ex ea commodo consequat.</p>
  <div class="quotes">
    <div class="quote"><div class="quote-box">Lorem Ipsum is simply dummy text of the printing and typesetting industry. Lorem Ipsum has been the industry's standard dummy text ever since the 1500s, when</div><div class="person"><span class="avatar" role="img" aria-label="Client portrait"></span><div><b>Dana Whitfield</b><span>Manager</span></div></div></div>
    <div class="quote"><div class="quote-box">Lorem Ipsum is simply dummy text of the printing and typesetting industry. Lorem Ipsum has been the industry's standard dummy text ever since the 1500s, when</div><div class="person"><span class="avatar" role="img" aria-label="Client portrait"></span><div><b>Marcus Hale</b><span>Manager</span></div></div></div>
    <div class="quote"><div class="quote-box">Lorem Ipsum is simply dummy text of the printing and typesetting industry. Lorem Ipsum has been the industry's standard dummy text ever since the 1500s, when</div><div class="person"><span class="avatar" role="img" aria-label="Client portrait"></span><div><b>Dana Whitfield</b><span>Manager</span></div></div></div>
  </div>
</div></section>

<footer class="footer"><div class="wrap">
  <div class="fcol"><h5>RESOURCES</h5><a>Resources</a><a>Testimonials</a><a>Competitions</a><a>Media Coverage</a><a>Crime Prevention</a></div>
  <div class="fcol wide"><h5>CUSTOMER SERVICE (888) 555-0147</h5><div class="split"><div><a>Affiliate Programs</a><a>FAQ</a><a>About Us</a><a>Contact Us</a></div><div><a>Returns/Exchange</a><a>Privacy</a><a>Warranty Information</a><a>Become A Distributor</a></div></div></div>
  <div class="fcol"><h5>FOLLOW US</h5><a>Social Feed</a><a>Updates</a><a>Video Channel</a><a>Blog</a></div>
  <div class="fcol last"><h5>RESOURCES</h5><p>US Patent Numbers 1,234,567 &amp; 7,654,321. Information Sources: National Crime Survey, Regional Safety Statistics &amp; Public Safety Council.</p><span class="seal"></span><span class="seal sm"></span></div>
</div></footer>

<div class="bottombar"><div class="wrap">
  <span>Copyright © 2005-2013 ShieldWorks Co LLC. All rights reserved.</span>
  <div class="cards"><span></span><span></span><span></span><span></span></div>
</div></div>

</body>
</html>
```